Wedding Decor and Entertianment business card

Company - We run a weddings and events company called Amber Finch, we provide most entertainment and decor services to our customers.

Initial idea is ....
A simple business card with logo on the front, this will be spot varnish. On a matt black background.
The reverse will be simple contact information.

But happy to try things outside of the box and would welcome some crazy ideas.

Target Market(s)

wedding couples - 21 - 40
High end wedding venues.

Industry/Entity Type

Wedding

Contact Information for Business Card

01492 718 263
amberfinchevents.co.uk
rowan@amberfinchevents.co.uk
or
helena@amberfinchevents.co.uk

Requirements
Nice to have
• black matt background with spot varnish logo on the front.

```html
<!DOCTYPE html>
<html lang="en">
<head>
<meta charset="utf-8">
<title>Amber Finch – Business Card</title>
<link href="https://fonts.googleapis.com/css2?family=Jost:wght@400&display=swap" rel="stylesheet">
<style>
  :root {
    --backdrop: #5b4b3d;
    --card-black: #0f0f10;
    --card-black-light: #1a1a1c;
    --varnish-silver: #c8c8ca;
    --accent-plum: #8a5a86;
    --contact-grey: #b9b9bb;
  }
  * { margin: 0; padding: 0; box-sizing: border-box; }
  html, body {
    width: 1200px;
    height: 987px;
    overflow: hidden;
  }
  body {
    background: var(--backdrop);
    font-family: "Jost", "Futura", sans-serif;
    position: relative;
  }
  .card {
    position: absolute;
    left: 293px;
    width: 615px;
    height: 351px;
    border-radius: 16px;
    background: linear-gradient(160deg, var(--card-black-light) 0%, var(--card-black) 55%);
    box-shadow: 0 2px 6px rgba(0, 0, 0, 0.35);
  }
  .card--front { top: 129px; }
  .card--back { top: 533px; }

  .brand {
    position: absolute;
    top: 176px;
    left: 50%;
    transform: translate(-50%, -50%);
    display: flex;
    align-items: center;
    gap: 20px;
    white-space: nowrap;
  }
  .brand__dot {
    width: 40px;
    height: 40px;
    border: 3px solid var(--varnish-silver);
    border-radius: 50%;
  }
  .brand__name {
    font-size: 29px;
    font-weight: 400;
    letter-spacing: 0.32em;
    color: var(--varnish-silver);
    text-transform: uppercase;
  }

  .back-brand {
    position: absolute;
    top: 52px;
    right: 42px;
    font-size: 17px;
    letter-spacing: 0.22em;
    color: var(--accent-plum);
    text-transform: uppercase;
  }
  .contact {
    position: absolute;
    left: 41px;
    top: 214px;
  }
  .contact__name {
    font-size: 23px;
    font-weight: 400;
    color: var(--accent-plum);
    text-transform: uppercase;
    letter-spacing: 0.02em;
    margin-bottom: 12px;
  }
  .contact__line {
    font-size: 15.5px;
    line-height: 21px;
    color: var(--contact-grey);
  }
</style>
</head>
<body>
  <section class="card card--front" aria-label="Card front">
    <div class="brand">
      <span class="brand__dot"></span>
      <span class="brand__name">Amber Finch</span>
    </div>
  </section>

  <section class="card card--back" aria-label="Card back">
    <div class="back-brand">Amber Finch</div>
    <div class="contact">
      <p class="contact__name">Rowan Pierce</p>
      <p class="contact__line">01492 718 263</p>
      <p class="contact__line">rowan@amberfinchevents.co.uk</p>
      <p class="contact__line">amberfinchevents.co.uk</p>
    </div>
  </section>
</body>
</html>
```